Bramblewick Keystone

Looking for modern business cards.
Clean contemporary design.
Similar to this.
https://www.snapvorlo.net/imgview?src=https%3A%2F%2Fcdn.printquell.net%2Fprofessional_elegant_modern_black_plain_metal_business_card-a1b2c3d4e5f60718293a4b5c6d7e8f90_qwxyz_4tmpl_540.jpg&ref=https%3A%2F%2Fwww.printquell.net%2Fprofessional_elegant_modern_black_plain_metal_business_card-100200300400500600&id=7aB9cD3e-QR5TU&tid=Xyz_abc123defGH%3A&v=10abcDEFghiJKLmnoPQRstUVwxYZ0123456789abcd..x&w=540&h=540&bih=1360&biw=1061&q=modern%20business%20cards&ref2=0abcDEFghiJKLmnoPQRstUVwxYZ0123456789abcd&ia=mrc&ua=8

But I'd like the blue to look metallic.

```html
<!DOCTYPE html>
<html lang="en">
<head>
<meta charset="utf-8">
<title>Bramblewick Keystone — Business Card</title>
<link rel="stylesheet" href="https://fonts.googleapis.com/css2?family=Signika:wght@300;400;600&display=swap">
<style>
  :root {
    --stage: #e9ecef;
    --card-white: #f3f8fa;
    --ink-teal: #2a8db4;
    --ink-navy: #2c5a86;
    --accent-red: #e8361f;
    --metal-deep: #1f4f8c;
    --metal-mid: #3e73b3;
    --metal-light: #8fb6e2;
    --metal-sheen: #d7e6f6;
    --text-on-blue: #eef4fb;
  }
  * { box-sizing: border-box; margin: 0; padding: 0; }
  html, body { width: 1200px; height: 902px; overflow: hidden; }
  body {
    background: var(--stage);
    font-family: "Signika", sans-serif;
    display: flex;
    align-items: center;
    justify-content: center;
    gap: 60px;
  }
  .card {
    width: 520px;
    height: 297px;
    border-radius: 6px;
    position: relative;
    overflow: hidden;
    box-shadow: 0 6px 18px rgba(0,0,0,.14);
  }

  /* Front */
  .card--front {
    background: var(--card-white);
    display: flex;
    padding: 0 36px 0 44px;
    align-items: center;
    justify-content: space-between;
  }
  .brand { display: flex; flex-direction: column; gap: 6px; }
  .brand__row { display: flex; align-items: center; gap: 10px; }
  .brand__name {
    font-weight: 600;
    font-size: 26px;
    color: var(--ink-navy);
    line-height: 1.05;
    width: 170px;
  }
  .brand__dot {
    width: 10px; height: 10px; border-radius: 50%;
    background: var(--accent-red);
    flex: none;
  }
  .brand__tagline {
    font-size: 9px;
    color: var(--ink-teal);
    letter-spacing: .2px;
  }
  .contacts { list-style: none; display: flex; flex-direction: column; gap: 20px; }
  .contact { display: flex; align-items: center; gap: 12px; color: var(--ink-teal); }
  .contact__icon {
    width: 32px; height: 32px; flex: none;
    border: 2px solid var(--ink-teal);
    border-radius: 50%;
    display: flex; align-items: center; justify-content: center;
  }
  .contact__icon svg { width: 16px; height: 16px; fill: var(--ink-teal); }
  .contact__text { font-size: 14px; font-weight: 300; line-height: 1.3; }
  .contact__text--phone { font-size: 20px; font-weight: 600; }

  /* Back */
  .card--back {
    background:
      radial-gradient(circle at 22% 30%, rgba(215,230,246,.45) 0 14%, transparent 32%),
      radial-gradient(circle at 40% 18%, rgba(215,230,246,.35) 0 4%, transparent 9%),
      linear-gradient(125deg, var(--metal-light) 0%, var(--metal-mid) 28%, var(--metal-deep) 48%, var(--metal-mid) 62%, var(--metal-sheen) 74%, var(--metal-mid) 86%, var(--metal-deep) 100%);
    display: flex;
    align-items: center;
    justify-content: center;
  }
  .back__url {
    position: absolute;
    left: 30px; top: 50%;
    transform: translateY(-50%) rotate(-90deg);
    transform-origin: left center;
    translate: 8px 95px;
    font-size: 11px;
    letter-spacing: 2px;
    color: var(--text-on-blue);
    white-space: nowrap;
  }
  .back__mark { display: flex; align-items: center; gap: 12px; }
  .back__name {
    font-weight: 600;
    font-size: 30px;
    color: var(--text-on-blue);
    text-shadow: 0 2px 4px rgba(10,30,60,.3);
  }
  .back__dot {
    width: 12px; height: 12px; border-radius: 50%;
    background: var(--accent-red);
  }
</style>
</head>
<body>

  <section class="card card--front" aria-label="Card front">
    <div class="brand">
      <div class="brand__row">
        <span class="brand__name">Bramblewick Keystone</span>
        <span class="brand__dot"></span>
      </div>
      <p class="brand__tagline">Executive Leadership On Demand</p>
    </div>

    <ul class="contacts">
      <li class="contact">
        <span class="contact__icon">
          <svg viewBox="0 0 24 24"><path d="M6.6 10.8a15.1 15.1 0 0 0 6.6 6.6l2.2-2.2a1 1 0 0 1 1-.25 11.4 11.4 0 0 0 3.6.57 1 1 0 0 1 1 1V20a1 1 0 0 1-1 1A17 17 0 0 1 3 4a1 1 0 0 1 1-1h3.5a1 1 0 0 1 1 1c0 1.25.2 2.45.57 3.57a1 1 0 0 1-.25 1z"/></svg>
        </span>
        <span class="contact__text contact__text--phone">555 014.2298</span>
      </li>
      <li class="contact">
        <span class="contact__icon">
          <svg viewBox="0 0 24 24"><path d="M12 3 2 12h3v8h5v-6h4v6h5v-8h3z"/></svg>
        </span>
        <span class="contact__text">Your Addres<br>Street Location, City</span>
      </li>
      <li class="contact">
        <span class="contact__icon">
          <svg viewBox="0 0 24 24"><path d="M3 6h18v12H3zm2 2v.3l7 4.6 7-4.6V8zm0 2.6V16h14v-5.4l-7 4.6z"/></svg>
        </span>
        <span class="contact__text">joe@bramblewick-keystone.com</span>
      </li>
    </ul>
  </section>

  <section class="card card--back" aria-label="Card back">
    <span class="back__url">www.bramblewick-keystone.com</span>
    <div class="back__mark">
      <span class="back__name">Bramblewick Keystone</span>
      <span class="back__dot"></span>
    </div>
  </section>

</body>
</html>
```